【画像サイズ】※MZSより抜粋
表紙ファイルの理想的な採寸は2,560×1,600ピクセルです。
注:画像の寸法は1,000×625ピクセル以上であることが必要です。
画像の最大の寸法は10,000×10,000ピクセルです。

【タイトル】
家族向け専任相談員がすすめる日々の工夫
ドキドキ平気!まあるい毎日の育ち術

サブキャッチ
心理学×四柱推命メソッド
我が子を上手に愛したいあなたへ

【著者】
ひだまりファミリーケア協会 もりした かなえ

【本の内容】
子どもを怒って、自分を責めてしまうお母様向けです。
子育ての悩みを、育児書やインターネット情報では効果がなかったり
どちらにも相談できなかったりする現状。
心理学×四柱推命メソッドで、お母様とお子様だけの簡単な解決方法を
やさしくお伝えします。
子どもと過ごすのが楽しくなり、母子ともに満たされ笑顔・Happyな暮らしを実現します。

※本文を参考資料として添付いたします。

【デザイン要望】
タイトル、サブキャッチと合わせて
読者様特典プレゼントのアピールもしたいです。

読者様特典として、イラストでやさしくわかりやすい!四柱推命電子書籍プレゼント

特にイメージにこだわりはありませんので、
自由な発想でのデザインご応募を楽しみにしております。

※次点、次々点の方への参加報酬を設定いたしました。

※その他、必要な情報がありましたら、お問い合わせください。
どうぞ、よろしくお願いいたします。

依頼のジャンルは、子育て・母親向け・育児法・心理学・学び・カウンセリング です。
カテゴリーに近いものがなく、ひとまず、資格・習い事としております。

優しい色使いと、見やすいタイトル、まとまり感でこちらに決定いたしました。

たくさんの素晴らしい商品にに感動しました。本当にありがとうございました。どちらも選びたくて本当に、迷いに迷いました。

```html
<!DOCTYPE html>
<html lang="ja">
<head>
<meta charset="utf-8">
<title>ドキドキ平気!まあるい毎日の育ち術</title>
<link href="https://fonts.googleapis.com/css2?family=M+PLUS+Rounded+1c:wght@500;700;800&display=swap" rel="stylesheet">
<style>
  :root {
    --bg-pink: #fbe1e7;
    --title-pink: #ec4f82;
    --deep-pink: #e9557f;
    --band-blue: #8fd0ee;
    --text-blue: #3a9bd3;
    --ink: #4a4a4a;
    --white: #ffffff;
    --art-main: #f6c2cf;
    --art-soft: #fde9d7;
  }
  * { margin: 0; padding: 0; box-sizing: border-box; }
  html, body { width: 750px; height: 1200px; overflow: hidden; }
  body { font-family: "M PLUS Rounded 1c", sans-serif; color: var(--ink); }
  .cover {
    position: relative; width: 750px; height: 1200px;
    background: var(--bg-pink); overflow: hidden;
  }
  .lead {
    position: absolute; top: 28px; left: 0; width: 100%;
    text-align: center; font-size: 31px; font-weight: 700; letter-spacing: 1px;
  }
  .title-line {
    position: absolute; color: var(--title-pink); font-weight: 800;
    line-height: 1; white-space: nowrap;
  }
  .title-first { top: 110px; left: 40px; font-size: 96px; letter-spacing: 8px; }
  .title-second { top: 218px; left: 0; width: 100%; text-align: center; font-size: 100px; letter-spacing: 4px; }
  .badge {
    position: absolute; top: 128px; left: 480px;
    font-size: 27px; font-weight: 800; color: var(--deep-pink);
    white-space: nowrap;
    transform: rotate(-10deg); transform-origin: left center;
  }
  .illustration {
    position: absolute; left: 60px; top: 350px; width: 520px; height: 540px;
    border-radius: 50% 50% 44% 44%;
    background: radial-gradient(circle at 50% 45%, var(--art-soft) 0%, var(--art-main) 70%, rgba(246,194,207,0) 100%);
  }
  .author {
    position: absolute; right: 30px; top: 790px; text-align: right;
  }
  .author-org { font-size: 20px; font-weight: 700; line-height: 1.3; }
  .author-name { font-size: 34px; font-weight: 700; margin-top: 12px; letter-spacing: 4px; line-height: 1.2; }
  .band {
    position: absolute; left: 0; top: 910px; width: 100%; height: 118px;
    background: var(--band-blue); text-align: center;
  }
  .band-method {
    display: inline-block; margin-top: 12px; padding: 2px 24px;
    background: var(--white); color: var(--text-blue);
    font-size: 34px; font-weight: 800; border-radius: 4px;
  }
  .band-message { margin-top: 8px; font-size: 32px; font-weight: 700; color: var(--white); }
  .bonus {
    position: absolute; left: 30px; top: 1045px; width: 690px; height: 130px;
    background: var(--white); border-radius: 14px;
    display: flex; align-items: center;
  }
  .bonus-tag {
    margin-left: 16px; width: 108px; height: 108px; border-radius: 10px;
    background: var(--deep-pink); color: var(--white);
    font-size: 26px; font-weight: 800; line-height: 1.25;
    display: flex; align-items: center; justify-content: center; text-align: center;
  }
  .bonus-text { flex: 1; text-align: center; color: var(--deep-pink); }
  .bonus-note { font-size: 27px; font-weight: 700; transform: rotate(-3deg); }
  .bonus-gift { font-size: 34px; font-weight: 800; line-height: 1.2; margin-top: 4px; }
</style>
</head>
<body>
  <main class="cover">
    <p class="lead">家族向け専任相談員がすすめる日々の工夫</p>
    <h1>
      <span class="title-line title-first">まあるい</span>
      <span class="badge">ドキドキ平気!</span>
      <span class="title-line title-second">毎日の育ち術</span>
    </h1>
    <div class="illustration" role="img" aria-label="赤ちゃんを抱いてほほえむお母さんのやさしいイラストとハートの飾り"></div>
    <div class="author">
      <p class="author-org">ひだまり<br>ファミリーケア協会</p>
      <p class="author-name">もりした かなえ</p>
    </div>
    <section class="band">
      <p class="band-method">心理学×四柱推命メソッド</p>
      <p class="band-message">我が子を上手に愛したいあなたへ</p>
    </section>
    <section class="bonus">
      <div class="bonus-tag">読者様<br>特典</div>
      <div class="bonus-text">
        <p class="bonus-note">イラストでやさしくわかりやすい!</p>
        <p class="bonus-gift">四柱推命電子書籍<br>プレゼント</p>
      </div>
    </section>
  </main>
</body>
</html>
```